Flyer promoting Veltrane's workshops and credentials

We run Training workshops for the data analyst community. We'd like a flyer to sell our services using a style and colour scheme consistent with our website www.veltranepartners.co.uk . I've attached some background info and some existing e-brochures for different workshops to give a flavour for content (but these are poorly designed and we don't want a similar design!!). There's also an overview document which gives more direction. The flyer will be sent with an accompanying letter to Learning & Development decision makers as well as Anlaytical team managers. It's purpose would be to generate enquiries and bookings for primarliy our flagship workshop 'Turning Figures Into Real Gains'.

Target Market(s)

Learning and Development senior managers
Analytical team managers

Industry/Entity Type

Training

Other font styles liked:
• Similar to website for consistency

Requirements
Must have
• Good copy! Slick design more in line with European (UK) style advertising rather than US.
Nice to have
• Some humour,
Should not have
• should not be as boring and non-sales based as the website!! Website is not a great example!

```html
<!DOCTYPE html>
<html lang="en">
<head>
<meta charset="utf-8">
<title>Veltrane – Workshops for Data Analysts</title>
<link href="https://fonts.googleapis.com/css2?family=Oswald:wght@500;600&family=Lato:wght@300;400;700;900&display=swap" rel="stylesheet">
<style>
  :root {
    --orange: #f7841f;
    --orange-deep: #ee6d0c;
    --blue: #1a4a9c;
    --blue-deep: #123c85;
    --navy-text: #1c3f7a;
    --ink: #2a2a2a;
    --paper: #ffffff;
    --photo-light: #eef1f5;
    --photo-mid: #d7dde5;
  }
  * { box-sizing: border-box; margin: 0; padding: 0; }
  html, body { width: 834px; height: 1200px; overflow: hidden; background: var(--paper); }
  body { position: relative; font-family: "Lato", Arial, sans-serif; color: var(--ink); }

  .hero-photo {
    position: absolute; left: 0; top: 0; width: 834px; height: 380px;
    background: linear-gradient(100deg, var(--photo-light) 0%, #f6ece6 35%, #f3d3c4 45%, var(--photo-light) 62%, var(--photo-mid) 100%);
  }
  .brand-name {
    position: absolute; left: 560px; top: 58px;
    font-family: "Lato", Arial, sans-serif; font-weight: 700; font-size: 62px;
    color: var(--navy-text); letter-spacing: -1px;
  }
  .page-curve { position: absolute; left: 0; top: 220px; width: 834px; height: 160px; z-index: 1; }
  .advantages-panel {
    position: absolute; left: 518px; top: 282px; width: 316px; height: 575px; z-index: 2;
    background: linear-gradient(160deg, var(--blue) 0%, var(--blue-deep) 100%);
    border-bottom-left-radius: 90px;
  }
  .wave-bands { position: absolute; left: 0; top: 220px; width: 834px; height: 160px; z-index: 3; }

  .tag {
    position: absolute; z-index: 4; height: 32px; line-height: 32px;
    font-family: "Oswald", Arial, sans-serif; font-weight: 500; font-size: 20px;
    color: #fff; letter-spacing: 0.5px; padding-left: 20px;
    border-radius: 0 16px 16px 0;
  }
  .tag--orange { background: var(--orange); }
  .tag--blue { background: var(--blue); }
  .tag--advantages { left: 508px; top: 390px; width: 176px; }
  .tag--about { left: 0; top: 578px; width: 218px; }
  .tag--testimonials { left: 0; top: 898px; width: 178px; }

  .advantages-list {
    position: absolute; left: 548px; top: 440px; width: 270px; z-index: 4;
    list-style: none; color: #fff; font-weight: 700; font-size: 15.5px; line-height: 1.3;
  }
  .advantages-list li { position: relative; padding-left: 22px; margin-bottom: 19px; }
  .advantages-list li::before {
    content: ""; position: absolute; left: 2px; top: 6px; width: 7px; height: 7px;
    border-radius: 50%; background: var(--orange);
  }

  .headline {
    position: absolute; left: 20px; top: 420px;
    font-family: "Oswald", Arial, sans-serif; font-weight: 600; font-size: 74px;
    color: var(--orange); letter-spacing: 0.5px; line-height: 1;
  }
  .subheadline {
    position: absolute; left: 22px; top: 505px;
    font-family: "Lato", Arial, sans-serif; font-weight: 400; font-size: 31px;
    color: var(--ink); letter-spacing: 1px;
  }

  .body-copy {
    position: absolute; left: 20px; width: 455px;
    font-size: 14.6px; line-height: 1.37; text-align: justify; color: var(--ink);
  }
  .body-copy--about { top: 622px; }
  .body-copy--aim { top: 790px; }
  .highlight { color: var(--orange); font-weight: 700; }

  .testimonial { position: absolute; left: 20px; width: 455px; font-size: 14.6px; line-height: 1.37; text-align: justify; }
  .testimonial--one { top: 948px; }
  .testimonial--two { top: 1060px; }
  .testimonial blockquote { font-weight: 700; }
  .testimonial cite { display: block; font-style: italic; font-weight: 700; color: var(--navy-text); }

  .skills-list { position: absolute; left: 556px; top: 892px; list-style: none; }
  .skills-list li { display: flex; align-items: center; height: 48px; margin-bottom: 20px; font-weight: 700; font-size: 21px; color: var(--ink); }
  .skill-icon { width: 44px; height: 44px; margin-right: 14px; flex: none; }

  .contact-block {
    position: absolute; left: 492px; top: 1108px; width: 342px; height: 92px;
    background: var(--orange); border-top-left-radius: 46px;
    padding: 12px 0 0 62px; color: #fff; font-weight: 700; font-size: 17px; line-height: 1.5;
  }
  .contact-block div { display: flex; align-items: center; }
  .contact-block svg { width: 12px; height: 12px; margin-right: 8px; flex: none; }
  .footer-strip { position: absolute; left: 0; bottom: 0; width: 834px; height: 10px; background: var(--orange); }
</style>
</head>
<body>
  <div class="hero-photo" role="img" aria-label="Smiling woman in an orange blazer at a laptop holding a bank card, with a rising bar and line chart behind her"></div>
  <div class="brand-name">Veltrane</div>

  <svg class="page-curve" viewBox="0 0 834 160" aria-hidden="true">
    <path d="M0,150 C230,185 520,95 834,58 L834,160 L0,160 Z" fill="#fff"/>
  </svg>
  <div class="advantages-panel"></div>
  <svg class="wave-bands" viewBox="0 0 834 160" aria-hidden="true">
    <path d="M0,92 C200,150 480,58 834,18 L834,42 C500,80 220,168 0,122 Z" fill="#f7841f"/>
    <path d="M0,122 C220,168 500,80 834,42 L834,62 C520,98 230,188 0,150 Z" fill="#1a4a9c"/>
  </svg>

  <div class="tag tag--orange tag--advantages">ADVANTAGES</div>
  <ul class="advantages-list">
    <li>CPD accredited</li>
    <li>Unique</li>
    <li>99.4% of past attendees would recommend the workshop to other analysts</li>
    <li>Has plenty of positive testimonials</li>
    <li>Been attended by UK's largest organisations and regularly by some.</li>
    <li>Been running for over 10 years</li>
    <li>Cornerstone workshop in the development of analysts</li>
  </ul>

  <h1 class="headline">WORKSHOPS</h1>
  <p class="subheadline">FOR DATA ANALYSTS</p>

  <div class="tag tag--blue tag--about">ABOUT WORKSHOP</div>
  <p class="body-copy body-copy--about">Our workshops have been attended by many of the UK's largest organisations and many international organisations too including Korvane, Meridell Bank, Brightfuel and XXX. Our workshops are run by experienced professionals including Martin Askew, Veltrane's founder and the facilitator for Veltrane's flagship workshop 'Turning Figures Into Real Gains' - a workshop that has been running for <span class="highlight">over 10 years and become an essential</span> 'cornerstone' development session for many of our regular clients' analysts.</p>
  <p class="body-copy body-copy--aim">We aim for our workshops to be educational, interactive, practical and fun – we believe we deliver on this but don't just take our word for it, here are some comments from our clients.</p>

  <div class="tag tag--blue tag--testimonials">TESTIMONIALS</div>
  <div class="testimonial testimonial--one">
    <blockquote>“We took from the course a number of actionable learnings that we have put into practice and this has resulted in positive feedback and a happier more valued team. Recommend the course to new and experienced analysts alike.”</blockquote>
    <cite>— Dan Pellow, Harbourline Trust</cite>
  </div>
  <div class="testimonial testimonial--two">
    <blockquote>"One of the best courses I have been on. Very intuitive and has given me clear strategies on analysis to take back to my workplace."</blockquote>
    <cite>- Lucy Marden, Signalwave</cite>
  </div>

  <ul class="skills-list">
    <li>
      <svg class="skill-icon" viewBox="0 0 44 44" aria-hidden="true"><circle cx="22" cy="22" r="20" fill="#1a4a9c" stroke="#f7841f" stroke-width="3"/><path d="M13,15 h18 v11 h-10 l-5,4 v-4 h-3 z" fill="none" stroke="#fff" stroke-width="2" stroke-linejoin="round"/></svg>
      Communication
    </li>
    <li>
      <svg class="skill-icon" viewBox="0 0 44 44" aria-hidden="true"><circle cx="22" cy="22" r="20" fill="#1a4a9c" stroke="#f7841f" stroke-width="3"/><rect x="13" y="14" width="18" height="16" rx="1.5" fill="none" stroke="#fff" stroke-width="2"/><path d="M13,19 h18 M17,11 v5 M27,11 v5" stroke="#fff" stroke-width="2"/><rect x="16" y="22" width="3" height="3" fill="#fff"/><rect x="21" y="22" width="3" height="3" fill="#fff"/><rect x="26" y="22" width="3" height="3" fill="#fff"/></svg>
      Planning
    </li>
    <li>
      <svg class="skill-icon" viewBox="0 0 44 44" aria-hidden="true"><circle cx="22" cy="22" r="20" fill="#1a4a9c" stroke="#f7841f" stroke-width="3"/><rect x="12" y="13" width="20" height="14" fill="none" stroke="#fff" stroke-width="2"/><path d="M22,27 v5 M17,32 h10 M15,24 l5,-5 4,3 5,-6" fill="none" stroke="#fff" stroke-width="2"/></svg>
      Presentation Of Data
    </li>
  </ul>

  <div class="contact-block">
    <div><svg viewBox="0 0 12 12" aria-hidden="true"><path d="M2,1 l2.5,0 1,3 -1.5,1 a6,6 0 0 0 3,3 l1,-1.5 3,1 0,2.5 a1,1 0 0 1 -1,1 a10,10 0 0 1 -9,-9 a1,1 0 0 1 1,-1 z" fill="#fff"/></svg>0161 555 0142</div>
    <div><svg viewBox="0 0 12 12" aria-hidden="true"><rect x="1" y="3" width="10" height="7" fill="#fff"/><path d="M1,3 l5,4 5,-4" fill="none" stroke="#f7841f" stroke-width="1"/></svg>info@veltranepartners.co.uk</div>
    <div><svg viewBox="0 0 12 12" aria-hidden="true"><circle cx="6" cy="6" r="5" fill="#fff"/><path d="M1,6 h10 M6,1 c-3,3 -3,7 0,10 M6,1 c3,3 3,7 0,10" fill="none" stroke="#f7841f" stroke-width="0.8"/></svg>www.veltranepartners.co.uk</div>
  </div>
  <div class="footer-strip"></div>
</body>
</html>
```